Wine label for premium wine of vinery Vrbolanec.

Design Premium wine label.

The brand is called Melvara. Brand can be extended to Dorano Melvara. There
The label should be unique and high class feeling.
This is facebook lonk of the winery
https://www.pagebook.example/402918365510274/

On facebook you can see some examole of labels that are used now. Winery is called Vrbolanec, so they used letter "K" as a logo in different ways

Target Market(s)

Premium high class yet modern living traditional but also gadget fun.
I have uploaded few inspirational photos that the owner of the vinery likes. Hope it helps.

Industry/Entity Type

Vinery

Requirements
Must have
• Black, gold, silver color to be dominated. Colors that are NOT acceptable are: green, yellow, blue, purple, pink.

The name of the vinary is Vrbolanec and it should be on the front label.
Nice to have
• The size of label should fit the Grapely application screenshot frame.
Should not have
• Cheap perception of the label and brand

```html
<!DOCTYPE html>
<html lang="en">
<head>
<meta charset="utf-8">
<title>Melvara Sauvignon Blanc – Vrbolanec Label</title>
<link rel="stylesheet" href="https://fonts.googleapis.com/css2?family=Archivo:wght@700&family=Roboto+Condensed:wght@300;400&display=swap">
<style>
  :root {
    --page: #ffffff;
    --label-dark: #161616;
    --label-mid: #3b3b3b;
    --gold-light: #efe3b0;
    --gold: #cdb874;
    --gold-deep: #9c8a52;
    --ink: #111111;
    --silver: #e4e4e4;
    --silver-soft: #c9c9c9;
    --wine-red: #6e1a1f;
    --tear-white: #f6f6f6;
  }
  * { margin: 0; padding: 0; box-sizing: border-box; }
  html, body {
    width: 1200px;
    height: 1200px;
    overflow: hidden;
    background: var(--page);
  }
  .canvas {
    width: 1200px;
    height: 1200px;
    display: flex;
    align-items: center;
    justify-content: center;
  }
  .wine-label {
    position: relative;
    width: 800px;
    height: 894px;
    background: linear-gradient(90deg, var(--label-dark) 0%, var(--label-mid) 35%, #2a2a2a 70%, var(--label-dark) 100%);
    overflow: hidden;
  }
  .gold-band {
    position: absolute;
    top: 0;
    left: 0;
    width: 800px;
    height: 250px;
  }
  .winery-name {
    position: absolute;
    top: 52px;
    left: 0;
    width: 800px;
    text-align: center;
    font-family: "Archivo", sans-serif;
    font-weight: 700;
    font-size: 38px;
    letter-spacing: -0.5px;
    color: var(--ink);
  }
  .brand {
    position: absolute;
    top: 390px;
    left: 0;
    width: 800px;
    text-align: center;
  }
  .brand-name {
    font-family: "Roboto Condensed", sans-serif;
    font-weight: 300;
    font-size: 118px;
    letter-spacing: 2px;
    color: var(--gold);
    line-height: 1;
  }
  .brand-dot {
    position: absolute;
    top: 150px;
    left: 528px;
    width: 30px;
    height: 30px;
    border-radius: 50%;
    background: var(--wine-red);
  }
  .variety {
    position: absolute;
    top: 676px;
    left: 0;
    width: 800px;
    text-align: center;
    font-family: "Roboto Condensed", sans-serif;
    font-weight: 400;
    font-size: 42px;
    color: var(--silver);
    letter-spacing: 0.5px;
  }
  .variety-rule {
    position: absolute;
    top: 742px;
    left: 210px;
    width: 380px;
    height: 2px;
    background: linear-gradient(90deg, transparent, var(--silver-soft) 15%, var(--silver-soft) 85%, transparent);
  }
  .origin {
    position: absolute;
    top: 766px;
    left: 0;
    width: 800px;
    text-align: center;
    font-family: "Roboto Condensed", sans-serif;
    font-weight: 400;
    font-size: 33px;
    color: var(--silver-soft);
    letter-spacing: 1px;
  }
</style>
</head>
<body>
  <main class="canvas">
    <article class="wine-label">
      <svg class="gold-band" viewBox="0 0 800 250" width="800" height="250" aria-hidden="true">
        <defs>
          <linearGradient id="goldSheen" x1="0" y1="0" x2="1" y2="0">
            <stop offset="0" stop-color="#bfa963"/>
            <stop offset="0.25" stop-color="#efe3b0"/>
            <stop offset="0.55" stop-color="#e6d6a0"/>
            <stop offset="0.85" stop-color="#b9a462"/>
            <stop offset="1" stop-color="#9c8a52"/>
          </linearGradient>
          <linearGradient id="goldFade" x1="0" y1="0" x2="0" y2="1">
            <stop offset="0.55" stop-color="#000" stop-opacity="0"/>
            <stop offset="1" stop-color="#000" stop-opacity="0.35"/>
          </linearGradient>
        </defs>
        <path d="M0 0 H800 V218 L770 222 L740 216 L700 220 L660 212 L630 210 L600 224 L560 218 L520 222 L480 226 L440 220 L400 230 L370 224 L340 232 L300 226 L270 222 L230 228 L190 220 L150 224 L110 214 L80 218 L50 212 L20 220 L0 214 Z" fill="url(#goldSheen)"/>
        <path d="M0 0 H800 V218 L770 222 L740 216 L700 220 L660 212 L630 210 L600 224 L560 218 L520 222 L480 226 L440 220 L400 230 L370 224 L340 232 L300 226 L270 222 L230 228 L190 220 L150 224 L110 214 L80 218 L50 212 L20 220 L0 214 Z" fill="url(#goldFade)"/>
        <path d="M0 214 L20 220 L50 212 L80 218 L110 214 L150 224 L190 220 L230 228 L270 222 L300 226 L340 232 L370 224 L400 230 L440 220 L480 226 L520 222 L560 218 L600 224 L630 210 L660 212 L700 220 L740 216 L770 222 L800 218" fill="none" stroke="#f6f6f6" stroke-width="5" stroke-linejoin="round"/>
      </svg>
      <h2 class="winery-name">VRBOLANEC</h2>
      <div class="brand">
        <h1 class="brand-name">Melvara</h1>
        <span class="brand-dot"></span>
      </div>
      <p class="variety">SAUVIGNON BLANC</p>
      <div class="variety-rule"></div>
      <p class="origin">CROATIA</p>
    </article>
  </main>
</body>
</html>
```